Lumara Health & Wellness Business Card Design

We would like to create business cards matching with our new logo design. The card should be professional looking but still have a playful side and something that would be eye catching. We are planing to open a luxury medical spa and looking to create a design based on this new logo. We are looking for a design that shows off luxury but not be gold in color. Also, while we are a more female oriented medical center we do have men that come in for our services and it should be be too feminine.

Target Market(s)

Health & Wellness. Medical patients. Luxury spa

Industry/Entity Type

Health And Wellness

Contact Information for Business Card

It should have the logo design in the front of card and back of card should have our contact information. Our current colors are peach/ coral, teal, and gray. We are looking for a modern looking design.

Font styles to use
Script

Colors
32a6d6
e667a6
86cfc6
fece3e

Requirements
Must have
• It should have our logo design. We would prefer to have a more modern look to the card.
Nice to have
• Eye-Catching Design on the personable side but still classy.
Should not have
• At this point we are looking for the best design. It should not have color purple.

```html
<!DOCTYPE html>
<html lang="en">
<head>
<meta charset="utf-8">
<title>Lumara Health &amp; Wellness Business Card</title>
<link rel="stylesheet" href="https://fonts.googleapis.com/css2?family=Lato:wght@400&family=Cormorant+Garamond:ital,wght@1,500&display=swap">
<style>
  :root {
    --backdrop: #e4e7ea;
    --pink: #e667a6;
    --teal: #86cfc6;
    --blue: #32a6d6;
    --yellow: #fece3e;
    --white: #ffffff;
    --paper: #fbfbfb;
    --ink: #111111;
  }
  * { margin: 0; padding: 0; box-sizing: border-box; }
  html, body {
    width: 1200px; height: 1200px; overflow: hidden;
    background: var(--backdrop);
    font-family: "Lato", sans-serif;
    color: var(--ink);
  }
  .canvas { position: relative; width: 1200px; height: 1200px; }
  .card {
    position: absolute; left: 156px; width: 894px; height: 516px;
    box-shadow: 0 6px 14px rgba(0,0,0,0.28);
    overflow: hidden;
  }
  .card-front { top: 78px; }
  .card-back { top: 633px; background: var(--teal); }
  .front-art { position: absolute; inset: 0; width: 100%; height: 100%; display: block; }
  .logo-panel {
    position: absolute; left: 204px; top: 122px; width: 488px; height: 216px;
    background: var(--white);
    display: flex; align-items: center; justify-content: center;
  }
  .logo-panel::after {
    content: ""; position: absolute; inset: 6px;
    border: 1.5px solid var(--ink);
  }
  .brand-name {
    font-family: "Lato", sans-serif; font-weight: 400; color: var(--ink);
    text-align: center; line-height: 1.1;
  }
  .brand-name .brand-main { display: block; font-size: 66px; letter-spacing: 2px; }
  .brand-name .brand-sub { display: block; font-size: 25px; letter-spacing: 1px; margin-top: 6px; }
  .back-inner {
    position: absolute; inset: 18px; background: var(--paper);
  }
  .back-logo {
    position: absolute; left: 42px; top: 160px; width: 350px;
    display: flex; justify-content: center;
  }
  .back-logo .brand-main { font-size: 60px; }
  .back-logo .brand-sub { font-size: 22px; }
  .divider {
    position: absolute; left: 420px; top: 114px; width: 3px; height: 250px;
    background: var(--ink);
  }
  .contact {
    position: absolute; left: 440px; top: 128px; width: 390px; text-align: center;
  }
  .contact-title {
    font-family: "Cormorant Garamond", serif; font-style: italic; font-weight: 500;
    font-size: 56px; line-height: 1; margin-bottom: 20px;
  }
  .contact-list { list-style: none; font-size: 20px; line-height: 29px; }
</style>
</head>
<body>
<main class="canvas">
  <section class="card card-front" aria-label="Card front">
    <svg class="front-art" viewBox="0 0 596 344" preserveAspectRatio="none" role="img" aria-label="Colour-block background in pink, teal, blue and yellow with marbled texture">
      <rect width="596" height="344" fill="var(--teal)"/>
      <polygon points="0,0 560,0 0,135" fill="var(--pink)"/>
      <polygon points="560,0 596,0 596,344 330,344" fill="var(--blue)"/>
      <polygon points="0,168 338,344 0,344" fill="var(--yellow)"/>
    </svg>
    <div class="logo-panel">
      <p class="brand-name"><span class="brand-main">Lumara</span><span class="brand-sub">Health &amp; Wellness</span></p>
    </div>
  </section>

  <section class="card card-back" aria-label="Card back">
    <div class="back-inner">
      <div class="back-logo">
        <p class="brand-name"><span class="brand-main">Lumara</span><span class="brand-sub">Health &amp; Wellness</span></p>
      </div>
      <div class="divider"></div>
      <div class="contact">
        <h2 class="contact-title">contact us</h2>
        <ul class="contact-list">
          <li>(555) 014-2280</li>
          <li>hello@lumarawellness.com</li>
          <li>42 Linden Ave, Suite 4 Fairview, NJ 07099</li>
          <li>www.lumarawellness.com</li>
        </ul>
      </div>
    </div>
  </section>
</main>
</body>
</html>
```